Portfolio required for virtual assistant seeking new clients

I require an editable Word template that can be sent to clients. This is a new business venture I am undertaking - working as a virtual assistant (administration work). I will need to find my own clients so would like Wow factor. Target group will be small businesses/legal industry so needs to look professional.
The portfolio will need to note information about me, why hire me, my skill set and credentials. May add testimonials too. I have attached a draft of the amount of text required - still working on this.
I will upload my logo and business card design. I do like consistency.
Colours used Pantone 2745 C and 272 C. Open to other colours but would like to see the main colours of logo incorporated. Images welcome. May insert an image of myself at some stage so please allow for a spot for this photo.
The portfolio will need to be converted to pdf to send by email as well as printable.
Updates

Automatically set for 24 hours apologies did not see this. Now amended

```html
<!DOCTYPE html>
<html lang="en">
<head>
<meta charset="utf-8">
<title>Mara Lent – Virtual Assistant Portfolio</title>
<link rel="stylesheet" href="https://fonts.googleapis.com/css2?family=Montserrat:ital,wght@0,400;0,500;0,600;0,700;0,800;1,400&display=swap">
<style>
  :root{
    --navy:#22367e;
    --navy-deep:#1e2f72;
    --periwinkle:#5b74b4;
    --band:#5469a9;
    --paper:#f4f4f5;
    --paper-grey:#ececee;
    --panel:#e2e3e8;
    --ink:#1c1f2b;
    --white:#ffffff;
    --bg:#f5f5f5;
  }
  *{box-sizing:border-box;margin:0;padding:0}
  html,body{width:1200px;height:1200px;overflow:hidden;background:var(--bg)}
  body{font-family:"Montserrat",sans-serif;color:var(--ink);position:relative}

  .page{position:absolute;top:218px;width:540px;height:764px;overflow:hidden;box-shadow:0 6px 24px rgba(0,0,0,.12)}
  .page--intro{left:40px;background:var(--paper)}
  .page--services{left:620px;background:var(--paper-grey)}

  /* Intro page */
  .intro-top{position:absolute;left:0;top:0;width:540px;height:545px;background:var(--navy)}
  .brand{position:absolute;left:28px;top:30px;display:flex;align-items:center;gap:6px;color:var(--periwinkle);font-weight:700;font-size:13px;letter-spacing:.04em}
  .brand__dot{width:10px;height:10px;border-radius:50%;background:var(--periwinkle)}
  .title{position:absolute;right:30px;top:36px;text-align:right;color:var(--white)}
  .title__name{font-weight:600;font-size:42px;letter-spacing:.08em;line-height:1}
  .title__role{font-weight:400;font-size:19px;letter-spacing:.04em;margin-top:4px}
  .title-rule{position:absolute;left:28px;right:30px;top:118px;height:1.5px;background:var(--white)}

  .portrait{position:absolute;left:30px;top:140px;width:170px;height:200px;border:5px solid var(--white);background:linear-gradient(160deg,#eeeeee,#d9d6d3 60%,#a78a74)}
  .contact{position:absolute;left:34px;top:362px;width:176px;height:183px;background:var(--periwinkle);padding:20px 14px;color:var(--white);font-size:8.5px;line-height:1}
  .contact__row{display:flex;align-items:center;gap:8px;margin-bottom:12px}
  .contact__row svg{width:11px;height:11px;flex:none}
  .contact__row--plain{padding-left:19px}

  .section-head{display:flex;align-items:center;gap:8px;font-weight:800;font-size:11px;letter-spacing:.1em;text-transform:uppercase}
  .section-head::before{content:"";width:8px;height:8px;border-radius:50%;background:currentColor}
  .about{position:absolute;left:230px;top:148px;width:284px;color:var(--white)}
  .about .section-head{margin-bottom:10px}
  .body-text{font-size:7.6px;line-height:1.38;text-align:justify}
  .body-text p+p{margin-top:8px}

  .why{position:absolute;left:32px;top:565px;width:476px}
  .why .section-head{color:var(--navy);margin-bottom:10px}
  .why .body-text{color:var(--ink);text-align:left}

  .foot-band{position:absolute;left:0;bottom:0;width:540px;height:24px;background:var(--band)}

  /* Services page */
  .services-head{position:absolute;left:40px;top:40px;color:var(--navy)}
  .services-head .section-head{font-size:12px}
  .admin-panel{position:absolute;left:40px;top:72px;width:230px;height:412px;background:var(--panel);padding:16px 16px}
  .skill-group{margin-bottom:12px}
  .skill-group h3{font-weight:700;font-size:8.5px;letter-spacing:.06em;text-transform:uppercase;margin-bottom:5px;color:var(--ink)}
  .skill-group ul{list-style:none}
  .skill-group li{font-size:7.6px;line-height:1.35;display:flex;gap:5px;margin-bottom:2px}
  .skill-group li svg{width:7px;height:7px;flex:none;margin-top:2px}
  .skills-right{position:absolute;left:290px;top:82px;width:220px}

  .credentials{position:absolute;left:40px;top:510px;width:250px;height:180px;background:var(--navy);padding:16px 18px;color:var(--white)}
  .credentials .section-head{margin-bottom:12px}
  .credential{border-bottom:1px solid rgba(255,255,255,.7);padding:5px 0 6px;font-size:7.8px;line-height:1.3;letter-spacing:.04em;text-transform:uppercase}
  .credential strong{font-weight:700;display:block}
</style>
</head>
<body>

<section class="page page--intro">
  <div class="intro-top">
    <div class="brand"><span class="brand__dot"></span>Mara Lent</div>
    <header class="title">
      <h1 class="title__name">MARA LENT</h1>
      <p class="title__role">VIRTUAL ASSISTANT</p>
    </header>
    <div class="title-rule"></div>

    <div class="portrait" role="img" aria-label="Portrait photo of the virtual assistant"></div>

    <div class="contact">
      <div class="contact__row">
        <svg viewBox="0 0 12 12"><circle cx="6" cy="6" r="5.3" fill="none" stroke="#fff" stroke-width="1"/><rect x="3.3" y="4.2" width="5.4" height="3.6" fill="none" stroke="#fff" stroke-width=".8"/><path d="M3.3 4.2 6 6.2 8.7 4.2" fill="none" stroke="#fff" stroke-width=".8"/></svg>
        emailaddress@mailbox.com
      </div>
      <div class="contact__row">
        <svg viewBox="0 0 12 12"><circle cx="6" cy="6" r="5.3" fill="none" stroke="#fff" stroke-width="1"/><path d="M4.2 3.6c-.6.6-.4 1.9.8 3.2s2.5 1.6 3.1 1l.4-.6-1.1-.8-.5.4c-.5-.2-1.3-1-1.5-1.5l.4-.5-.8-1.1z" fill="#fff"/></svg>
        +1 555 0142
      </div>
      <div class="contact__row contact__row--plain">ABN #5120934</div>
    </div>

    <div class="about">
      <h2 class="section-head">About me</h2>
      <div class="body-text">
        <p>Hello, I'm Mara Lent, a mother, coffee lover, and a passion for travel. I enjoy organisation and making life easy. With over 15 years of experience in the legal field, I have gained valuable experience whilst at the same time, perfecting my skills.</p>
        <p>Throughout my journey in the legal profession, I have held various roles, each contributing to my growth and expertise. Starting as a Rounds Clerk, I quickly advanced to the role of Administrative Assistant in the area of Litigation which involved leading a team of administration assistants focused on supporting legal professionals and litigation processes. This role was invaluable in that it taught me the importance of organisation, time management, attention to detail and multitasking.</p>
        <p>I then transitioned into Debt Recovery, where I thrived as a Paralegal. In this role, I took on the responsibility of managing my own caseload and providing comprehensive legal support independently. Attention to detail, meticulous research and effective communication became second nature. This allowed me to achieve successful resolutions while maintaining the utmost organization and professionalism.</p>
      </div>
    </div>
  </div>

  <div class="why">
    <h2 class="section-head">Why hire me?</h2>
    <div class="body-text">
      <p>A virtual assistant is an affordable alternative to hiring on-site administration support. Hire me for a once-off task or on a regular basis. I'm here to help you so get more time back in your day so you can focus on more important tasks. I want to save you time, as who has enough of that these days!</p>
      <p>I am known for my reliability, determination, ability to work diligently in fast-paced environments as well as delivering results. I take pride in my meticulous approach to the tasks I undertake. I adapt well to new technology.</p>
      <p>I am excited to embrace new opportunities that allow me to showcase my skill set expertise, provide dedicated support to professionals and that may involve my legal expertise. I am committed to making a positive impact wherever I go, bringing efficiency and structure.</p>
    </div>
  </div>

  <div class="foot-band"></div>
</section>

<section class="page page--services">
  <div class="services-head"><h2 class="section-head">What can I do for you?</h2></div>

  <div class="admin-panel">
    <div class="skill-group">
      <h3>Administration</h3>
      <ul>
        <li><svg viewBox="0 0 8 8"><path d="M1 4.2 3 6 7 1.6" fill="none" stroke="#22367e" stroke-width="1.2"/></svg>Document preparation including editing</li>
        <li><svg viewBox="0 0 8 8"><path d="M1 4.2 3 6 7 1.6" fill="none" stroke="#22367e" stroke-width="1.2"/></svg>Data entry</li>
        <li><svg viewBox="0 0 8 8"><path d="M1 4.2 3 6 7 1.6" fill="none" stroke="#22367e" stroke-width="1.2"/></svg>Correspondence</li>
        <li><svg viewBox="0 0 8 8"><path d="M1 4.2 3 6 7 1.6" fill="none" stroke="#22367e" stroke-width="1.2"/></svg>Answering telephone calls</li>
        <li><svg viewBox="0 0 8 8"><path d="M1 4.2 3 6 7 1.6" fill="none" stroke="#22367e" stroke-width="1.2"/></svg>Email management</li>
        <li><svg viewBox="0 0 8 8"><path d="M1 4.2 3 6 7 1.6" fill="none" stroke="#22367e" stroke-width="1.2"/></svg>Diary management</li>
        <li><svg viewBox="0 0 8 8"><path d="M1 4.2 3 6 7 1.6" fill="none" stroke="#22367e" stroke-width="1.2"/></svg>Creating sub folders</li>
        <li><svg viewBox="0 0 8 8"><path d="M1 4.2 3 6 7 1.6" fill="none" stroke="#22367e" stroke-width="1.2"/></svg>Transcription</li>
      </ul>
    </div>
    <div class="skill-group">
      <h3>Travel management</h3>
      <ul>
        <li><svg viewBox="0 0 8 8"><path d="M1 4.2 3 6 7 1.6" fill="none" stroke="#22367e" stroke-width="1.2"/></svg>Booking appointments</li>
        <li><svg viewBox="0 0 8 8"><path d="M1 4.2 3 6 7 1.6" fill="none" stroke="#22367e" stroke-width="1.2"/></svg>Flights and transfers</li>
        <li><svg viewBox="0 0 8 8"><path d="M1 4.2 3 6 7 1.6" fill="none" stroke="#22367e" stroke-width="1.2"/></svg>Assist with car hire and accommodation</li>
        <li><svg viewBox="0 0 8 8"><path d="M1 4.2 3 6 7 1.6" fill="none" stroke="#22367e" stroke-width="1.2"/></svg>Arranging interstate travel</li>
      </ul>
    </div>
  </div>

  <div class="skills-right">
    <div class="skill-group">
      <h3>Software</h3>
      <ul>
        <li><svg viewBox="0 0 8 8"><path d="M1 4.2 3 6 7 1.6" fill="none" stroke="#22367e" stroke-width="1.2"/></svg>Office Suite</li>
        <li><svg viewBox="0 0 8 8"><path d="M1 4.2 3 6 7 1.6" fill="none" stroke="#22367e" stroke-width="1.2"/></svg>Practice Manager</li>
        <li><svg viewBox="0 0 8 8"><path d="M1 4.2 3 6 7 1.6" fill="none" stroke="#22367e" stroke-width="1.2"/></svg>CaseDesk</li>
      </ul>
    </div>
    <div class="skill-group">
      <h3>Debt collection</h3>
      <ul>
        <li><svg viewBox="0 0 8 8"><path d="M1 4.2 3 6 7 1.6" fill="none" stroke="#22367e" stroke-width="1.2"/></svg>Assist with sending out overdue statements</li>
        <li><svg viewBox="0 0 8 8"><path d="M1 4.2 3 6 7 1.6" fill="none" stroke="#22367e" stroke-width="1.2"/></svg>Issue demand letters</li>
        <li><svg viewBox="0 0 8 8"><path d="M1 4.2 3 6 7 1.6" fill="none" stroke="#22367e" stroke-width="1.2"/></svg>Issue claims and enforcement action in the local Magistrates Court</li>
        <li><svg viewBox="0 0 8 8"><path d="M1 4.2 3 6 7 1.6" fill="none" stroke="#22367e" stroke-width="1.2"/></svg>Negotiating payment arrangements</li>
        <li><svg viewBox="0 0 8 8"><path d="M1 4.2 3 6 7 1.6" fill="none" stroke="#22367e" stroke-width="1.2"/></svg>Knowledge with Court e-Filing portal</li>
      </ul>
    </div>
    <div class="skill-group">
      <h3>Other</h3>
      <ul>
        <li><svg viewBox="0 0 8 8"><path d="M1 4.2 3 6 7 1.6" fill="none" stroke="#22367e" stroke-width="1.2"/></svg>Online research</li>
        <li><svg viewBox="0 0 8 8"><path d="M1 4.2 3 6 7 1.6" fill="none" stroke="#22367e" stroke-width="1.2"/></svg>Event coordination</li>
      </ul>
    </div>
    <div class="skill-group">
      <h3>Legal</h3>
      <ul>
        <li><svg viewBox="0 0 8 8"><path d="M1 4.2 3 6 7 1.6" fill="none" stroke="#22367e" stroke-width="1.2"/></svg>Court e-Filing portal</li>
        <li><svg viewBox="0 0 8 8"><path d="M1 4.2 3 6 7 1.6" fill="none" stroke="#22367e" stroke-width="1.2"/></svg>Preparing Court documents</li>
        <li><svg viewBox="0 0 8 8"><path d="M1 4.2 3 6 7 1.6" fill="none" stroke="#22367e" stroke-width="1.2"/></svg>Filing Court Documents</li>
      </ul>
    </div>
  </div>

  <div class="credentials">
    <h2 class="section-head">Credentials</h2>
    <div class="credential"><strong>Certificate IV</strong>in Business (Legal Services)</div>
    <div class="credential"><strong>Certificate III</strong>of Business Administration</div>
    <div class="credential"><strong>Certificate II</strong>in Business</div>
  </div>

  <div class="foot-band"></div>
</section>

</body>
</html>
```